Brightway Elderplan (03)

We're designing a website to sell Medicare Supplements. Attached is the script we want to say and general layout, but please use your best knowledge to make it better. This platform should be extremely user-friendly, but we want to make it look fun and approachable! Most Insurance/medicare websites are very boring, drab, simple but we want this one to be more personalized, fun and sexy (but again, still user-friendly since our target demographic is 65+).

This homepage should include a fun and inviting quiz, the script is in the attachment below. It should also include the blurbs about what medicare supplements plans are and why they should buy them. Feel free to play around with cool fonts and imagery, we want the site to be engaging!

Target Market(s)

seniors

Industry/Entity Type

Insurance

Number of Pages Required

1 page

Requirements
Must have
• Quiz, company name and tag line, script
Nice to have
• fun, engaging elements

```html
<!DOCTYPE html>
<html lang="en">
<head>
<meta charset="utf-8">
<title>Brightway Elderplan</title>
<link href="https://fonts.googleapis.com/css2?family=IBM+Plex+Sans:wght@400;500;600&family=Montserrat:wght@600&display=swap" rel="stylesheet">
<style>
:root{
  --red:#e11b22;
  --ink:#111111;
  --text:#2b2b2b;
  --page:#f4f3f1;
  --card:#ffffff;
  --line:#c4c4c4;
  --tile:#f8f6f6;
  --footer:#000000;
  --footer-text:#e9e9e9;
}
*{margin:0;padding:0;box-sizing:border-box}
html,body{width:668px;height:1200px;overflow:hidden}
body{background:var(--page);font-family:"IBM Plex Sans",sans-serif;color:var(--text);position:relative}
.abs{position:absolute}

/* header */
.site-header{position:absolute;left:0;top:0;width:668px;height:41px;background:var(--card);box-shadow:0 1px 3px rgba(0,0,0,.08)}
.brand{position:absolute;left:74px;top:12px;font-family:"Montserrat",sans-serif;font-weight:600;font-size:13.5px;color:var(--ink)}
.nav{position:absolute;top:17px;font-size:7px;font-weight:500;color:var(--ink);letter-spacing:.1px}
.call-icon{position:absolute;left:493px;top:12px}
.call-label{position:absolute;left:516px;top:10px;font-size:7px;font-weight:500;color:var(--ink)}
.call-number{position:absolute;left:516px;top:19px;font-size:11px;font-weight:500;color:var(--red)}

/* cards */
.card{position:absolute;left:73px;width:522px;background:var(--card)}
.quiz-card{top:71px;height:355px}
.info-card{top:444px;height:494px}
.quiz-title{position:absolute;left:19px;top:18px;font-size:13px;font-weight:500;color:var(--ink)}
.question{position:absolute;left:21px;width:482px;height:53px;border:1px solid var(--line)}
.question .legend{position:absolute;left:14px;top:-7px;background:var(--card);padding:0 7px;font-size:9px;font-weight:500;color:var(--ink);letter-spacing:.2px}
.options{position:absolute;left:19px;top:22px;display:flex;gap:20px;font-size:8.6px;color:var(--ink)}
.option{display:flex;align-items:center;gap:5px}
.radio{width:10px;height:10px;border:1.2px solid var(--red);border-radius:50%;display:inline-block;position:relative}
.radio.on{background:var(--red)}
.radio.on::after{content:"";position:absolute;left:2.6px;top:1.2px;width:2.6px;height:4.6px;border:solid #fff;border-width:0 1.3px 1.3px 0;transform:rotate(45deg)}
.zip-label{position:absolute;left:22px;top:278px;font-size:9px;font-weight:500;color:var(--ink)}
.zip-field{position:absolute;left:23px;top:298px;width:197px;height:33px;border:2px solid #cfcfcf;display:flex;align-items:center;padding-left:10px;gap:8px;font-size:10.5px;color:#555}

.section-title{position:absolute;left:22px;font-size:9px;font-weight:500;color:var(--ink);letter-spacing:.1px}
.photo{position:absolute;left:23px;top:53px;width:188px;height:141px;background:linear-gradient(120deg,#6b5a2a 0%,#8a7a3a 30%,#3f7fb8 55%,#7d8070 80%,#4a5a2a 100%)}
.intro{position:absolute;left:225px;top:55px;width:276px;font-size:7.3px;line-height:9.8px}
.benefits{position:absolute;left:229px;list-style:none;font-size:7.3px;line-height:9.8px}
.benefits li{position:relative;padding-left:10px;margin-bottom:7px;width:230px}
.benefits li svg{position:absolute;left:0;top:2px}
.costs-intro{position:absolute;left:22px;top:246px;width:450px;font-size:7.3px;line-height:9.8px}
.tile{position:absolute;top:292px;width:142px;height:146px;background:var(--tile);border:1px solid #d9d6d6;text-align:center}
.tile svg{display:block;margin:16px auto 0}
.tile h3{margin-top:8px;font-size:8.5px;font-weight:500;line-height:11.7px;color:var(--ink)}
.tile p{margin:6px auto 0;width:118px;font-size:7.2px;line-height:8.9px}
.note{position:absolute;left:25px;top:453px;width:440px;font-size:7.3px;line-height:9.8px;color:var(--ink)}

/* footer */
.site-footer{position:absolute;left:0;top:973px;width:668px;height:227px;background:var(--footer);color:var(--footer-text)}
.footer-brand{position:absolute;left:80px;top:72px;font-family:"Montserrat",sans-serif;font-weight:600;font-size:13.5px;color:#fff}
.footer-head{position:absolute;top:30px;font-size:8px;font-weight:600;letter-spacing:.5px;color:#fff}
.footer-menu{position:absolute;left:260px;top:55px;list-style:none;font-size:7.5px;line-height:13.3px}
.footer-row{position:absolute;display:flex;align-items:center;gap:7px;font-size:7.5px;line-height:10.7px}
.dot{width:16px;height:16px;border-radius:50%;background:#fff;display:flex;align-items:center;justify-content:center;flex:none}
.footer-rule{position:absolute;left:67px;top:176px;width:522px;height:1px;background:#333}
.copyright{position:absolute;left:0;top:196px;width:654px;text-align:center;font-size:6px;color:#ddd}
</style>
</head>
<body>

<header class="site-header">
  <div class="brand">Brightway Elderplan</div>
  <span class="nav" style="left:246px">HOME</span>
  <span class="nav" style="left:282px">ABOUT US</span>
  <span class="nav" style="left:332px">MEDICARE</span>
  <span class="nav" style="left:387px">BLOG</span>
  <span class="nav" style="left:424px">GET QUOTES</span>
  <svg class="call-icon" width="18" height="18" viewBox="0 0 24 24" fill="none" stroke="#e11b22" stroke-width="1.6" stroke-linecap="round" stroke-linejoin="round"><path d="M22 16.9v3a2 2 0 0 1-2.2 2 19.8 19.8 0 0 1-8.6-3.1 19.5 19.5 0 0 1-6-6A19.8 19.8 0 0 1 2.1 4.2 2 2 0 0 1 4.1 2h3a2 2 0 0 1 2 1.7c.1 1 .4 1.9.7 2.8a2 2 0 0 1-.5 2.1L8 9.9a16 16 0 0 0 6 6l1.3-1.3a2 2 0 0 1 2.1-.4c.9.3 1.8.6 2.8.7a2 2 0 0 1 1.7 2z"/><path d="M15 5a5 5 0 0 1 4 4M15 1a9 9 0 0 1 8 8"/></svg>
  <div class="call-label">Call for FREE quotes:</div>
  <div class="call-number">(800) 555-0142</div>
</header>

<section class="card quiz-card">
  <h1 class="quiz-title">QUIZ</h1>

  <div class="question" style="top:60px">
    <span class="legend">1. I AM</span>
    <div class="options" style="gap:28px">
      <span class="option"><span class="radio on"></span>Over 64 years old</span>
      <span class="option"><span class="radio"></span>64 years old</span>
      <span class="option"><span class="radio"></span>Under 64 years old</span>
    </div>
  </div>

  <div class="question" style="top:135px;height:52px">
    <span class="legend">2. I AM</span>
    <div class="options" style="top:21px">
      <span class="option"><span class="radio"></span>Male</span>
      <span class="option"><span class="radio"></span>Female</span>
      <span class="option"><span class="radio"></span>Unspecified</span>
    </div>
  </div>

  <div class="question" style="top:210px;height:52px">
    <span class="legend">3. I WANT TO SEE</span>
    <div class="options" style="top:21px">
      <span class="option"><span class="radio"></span>Free plans</span>
      <span class="option"><span class="radio"></span>Premium plans</span>
      <span class="option"><span class="radio"></span>All plans</span>
    </div>
  </div>

  <div class="zip-label">ENTER ZIP CODE</div>
  <div class="zip-field">
    <svg width="13" height="14" viewBox="0 0 24 26" fill="none" stroke="#8a8a8a" stroke-width="1.6"><path d="M12 24s-8-7.5-8-13a8 8 0 0 1 16 0c0 5.5-8 13-8 13z"/><circle cx="12" cy="11" r="3"/></svg>
    <span>638001</span>
  </div>
</section>

<section class="card info-card">
  <h2 class="section-title" style="top:32px">WHAT IS A MEDICARE SUPPLEMENT PLAN?</h2>
  <div class="photo" role="img" aria-label="Photo of a smiling senior couple on a park bench looking at a tablet"></div>
  <p class="intro">Each Medicare Supplement insurance plan offers a different level of basic benefits, but each lettered plan will include the same standardized basic benefits regardless of insurance company and location. Medicare Supplement insurance plans do not always cover vision, dental, long-term care, or hearing aids, but all plans must cover at least a portion of the following basic benefits:</p>
  <ul class="benefits" style="top:119px">
    <li><svg width="7" height="6" viewBox="0 0 10 8"><path d="M1 4l3 3 5-6" fill="none" stroke="#e11b22" stroke-width="2"/></svg>Medicare Part A coinsurance costs up to an additional 365 days after Medicare benefits are exhausted</li>
    <li><svg width="7" height="6" viewBox="0 0 10 8"><path d="M1 4l3 3 5-6" fill="none" stroke="#e11b22" stroke-width="2"/></svg>Medicare Part A hospice care coinsurance or copayments</li>
    <li><svg width="7" height="6" viewBox="0 0 10 8"><path d="M1 4l3 3 5-6" fill="none" stroke="#e11b22" stroke-width="2"/></svg>Medicare Part B coinsurance or copayments</li>
    <li><svg width="7" height="6" viewBox="0 0 10 8"><path d="M1 4l3 3 5-6" fill="none" stroke="#e11b22" stroke-width="2"/></svg>First three pints of blood used in a medical procedure</li>
  </ul>

  <h2 class="section-title" style="top:226px">MEDICARE SUPPLEMENT INSURANCE PLAN COSTS</h2>
  <p class="costs-intro">Although private insurance companies are required to offer the same basic benefits for each lettered plan, they do have the ability to charge different premiums. You might want to shop around to find a Medicare Supplement insurance plan that may fit your medical and financial needs. Insurance companies may price their plan premiums in any of the following ways:</p>

  <div class="tile" style="left:24px">
    <svg width="22" height="22" viewBox="0 0 24 24" fill="none" stroke="#e11b22" stroke-width="2.2" stroke-linecap="round"><path d="M21 11a9 9 0 1 1-4-7"/><path d="M8 11l4 4 9-10"/></svg>
    <h3>COMMUNITY<br>NO-AGE-RATED</h3>
    <p>These Medicare Supplement insurance plans chargepremiums that are the same across the board, regardless of age.</p>
  </div>
  <div class="tile" style="left:176px">
    <svg width="22" height="22" viewBox="0 0 24 24" fill="none" stroke="#e11b22" stroke-width="2.2" stroke-linecap="round"><path d="M21 11a9 9 0 1 1-4-7"/><path d="M8 11l4 4 9-10"/></svg>
    <h3>ISSUE-<br>AGE-RATED:</h3>
    <p>These plans base their premiums on your age when you first enrolled in the policy. Therefore, the younger you are when you enroll in this type of plan, the lower your premium will be.</p>
  </div>
  <div class="tile" style="left:327px">
    <svg width="22" height="22" viewBox="0 0 24 24" fill="none" stroke="#e11b22" stroke-width="2.2" stroke-linecap="round"><path d="M21 11a9 9 0 1 1-4-7"/><path d="M8 11l4 4 9-10"/></svg>
    <h3>ATTAINED-<br>AGE-RATED:</h3>
    <p>Like issue-age-rated, these plans base their premiums on the age you were when you first bought a policy, but unlike issue - age - rated, premiums increase as you get older.</p>
  </div>

  <p class="note">Please note that no matter what rating method an insurance company uses, premiums may increase over time for reasons other than age, such as inflation.</p>
</section>

<footer class="site-footer">
  <div class="footer-brand">Brightway Elderplan</div>

  <div class="footer-head" style="left:260px">MENU</div>
  <ul class="footer-menu">
    <li>HOME</li><li>ABOUT US</li><li>MEDICARE</li><li>BLOG</li><li>GET QUOTES</li>
  </ul>

  <div class="footer-head" style="left:359px">CONTACT US</div>
  <div class="footer-row" style="left:358px;top:55px">
    <span class="dot"><svg width="7" height="8" viewBox="0 0 24 26"><path d="M12 25s-8-7.5-8-14a8 8 0 0 1 16 0c0 6.5-8 14-8 14z" fill="#222"/><circle cx="12" cy="11" r="3" fill="#fff"/></svg></span>
    <span>2750 Maple Grove Road<br>Fairview, CA 90210</span>
  </div>
  <div class="footer-row" style="left:358px;top:89px">
    <span class="dot"><svg width="7" height="7" viewBox="0 0 24 24"><path d="M22 16.9v3a2 2 0 0 1-2.2 2A19.8 19.8 0 0 1 2.1 4.2 2 2 0 0 1 4.1 2h3a2 2 0 0 1 2 1.7l.7 2.8-1.8 3.4a16 16 0 0 0 6 6l3.4-1.8 2.8.7a2 2 0 0 1 1.8 2z" fill="#222"/></svg></span>
    <span>Call Us<br>555.010.2288</span>
  </div>
  <div class="footer-row" style="left:358px;top:123px">
    <span class="dot"><svg width="8" height="6" viewBox="0 0 24 18"><rect x="1" y="1" width="22" height="16" rx="2" fill="#222"/><path d="M2 3l10 7 10-7" fill="none" stroke="#fff" stroke-width="2"/></svg></span>
    <span>E mail Us<br>hello@brightwayelderplan.com</span>
  </div>

  <div class="footer-head" style="left:519px">FOLLOW US</div>
  <div class="footer-row" style="left:518px;top:55px"><span class="dot"></span><span>Like us on<br>SOCIALHUB</span></div>
  <div class="footer-row" style="left:518px;top:89px"><span class="dot"></span><span>Follow us on<br>CHIRPLINE</span></div>
  <div class="footer-row" style="left:518px;top:123px"><span class="dot"></span><span>Follow us on<br>WORKNET</span></div>

  <div class="footer-rule"></div>
  <div class="copyright">Copyright © 2020 All Rights Reserved</div>
</footer>

</body>
</html>
```